The Harbourlight Dental centre, the Zentrix of dentistry

New concept of running a dental practice by having a walk in practice
WE ARE A HUSBAND AND WIFE TEAM

Really modern and sophisticated, we want it to feel different from the traditional dental practice.
we want it split into different pages:CONTACT US
LOCATION: Information about our location since patients often confuse us with the practice across the road
ABOUT US:
Opening hours - & 7 Days, We offer a weekend service
WALK IN: We offer a walk in service for dental treatments
TREATMENTS we offer

DENTAL ADVICE: Free dentist advise call back- So a dentist will call you back for free to discuss

Target Market(s)

Everyone

Industry/Entity Type

Dental

Coding

Coded - Design and coding required

Number of Pages Required

5+ page

Requirements
Must have
• First page
• * changing pictures
• *opening times
• * our walk in concept I.e. no appointment needed
• *logo
• * links in to carely hub (online booking system in Australia)
• * address /phone number/email
• * possible videos
• Second page
• meet the team
• third page
• dental treatments/walk in treatments
• fourth page
• dental advice with vid nest videos
• Fifth page
• contact us/maps/ we get confused with the dental practice across the road
• We would also like a giving back page. In this please include the photo's below of our dental mission in Guatemala, where by we did treatment for patients as part of a charity.
Nice to have
• Changing pictures on the home screen
• videos linked to home page

```html
<!DOCTYPE html>
<html lang="en">
<head>
<meta charset="utf-8">
<title>The Harbourlight Dental Centre</title>
<link rel="stylesheet" href="https://fonts.googleapis.com/css2?family=Open+Sans:wght@300;400;600;700&display=swap">
<style>
:root{
  --blue:#1ba9e1;
  --green:#9dc43a;
  --ink:#555;
  --dark:#333538;
  --grey-bg:#f1f1f1;
  --line:#e3e3e3;
  --white:#fff;
}
*{box-sizing:border-box;margin:0;padding:0}
html,body{width:1200px;height:2406px;overflow:hidden}
body{font-family:"Open Sans",Arial,sans-serif;color:var(--ink);background:var(--white);position:relative}
.abs{position:absolute}
.top-rule{left:0;top:0;width:1200px;height:6px;background:linear-gradient(90deg,var(--green) 50%,var(--blue) 50%)}
/* header */
.brand{left:132px;top:30px;display:flex;align-items:center;gap:14px}
.brand-mark{width:60px;height:60px;border-radius:50%;background:var(--blue)}
.brand-name{font-size:29px;font-weight:700;color:var(--green);line-height:1}
.brand-name small{display:block;font-size:11px;letter-spacing:3px;margin-top:4px;font-weight:700}
.header-info{right:133px;top:46px;text-align:right;font-size:10.5px;color:#666}
.header-info span{margin-left:16px}
.header-contact{right:133px;top:67px;font-size:16px;color:var(--blue);display:flex;gap:26px}
.header-contact span{display:flex;align-items:center;gap:8px}
/* nav */
.main-nav{left:132px;top:125px;width:935px;height:53px;background:var(--green);display:flex}
.main-nav a{color:var(--white);font-size:12px;text-decoration:none;display:flex;align-items:center;justify-content:center;text-transform:uppercase}
.main-nav a.active{background:var(--blue)}
/* hero */
.hero{left:0;top:178px;width:1200px;height:364px;background:linear-gradient(180deg,#9cb3c9 0%,#e8e8e6 35%,#cfcac3 70%,#8d8780 100%)}
.hero-arrow{top:340px;color:#fff;font-size:18px;opacity:.8}
.strap-blue{left:0;top:542px;width:600px;height:71px;background:var(--blue);color:#fff;font-weight:700;font-size:14px;padding:16px 0 0 132px;line-height:1.45;text-transform:uppercase}
.strap-green{left:600px;top:542px;width:600px;height:71px;background:var(--green);color:#fff;font-weight:700;font-size:22px;display:flex;align-items:center;justify-content:center}
/* welcome */
.video-thumb{left:132px;top:667px;width:243px;height:193px;background:linear-gradient(135deg,#3a4660,#6e7a92 55%,#c9b6b6)}
.play{left:236px;top:744px;width:38px;height:38px;border-radius:50%;background:var(--blue);border:3px solid #fff}
.play::after{content:"";position:absolute;left:13px;top:9px;border-left:12px solid #fff;border-top:7px solid transparent;border-bottom:7px solid transparent}
.welcome-title{left:396px;top:658px;font-size:32px;font-weight:300;color:var(--green)}
.welcome-text{left:396px;top:706px;width:670px;font-size:11.5px;line-height:1.65;color:#666}
.welcome-box{left:396px;top:776px;width:671px;height:84px;border:2px solid var(--green);padding:16px 28px;color:var(--green);font-size:16px;line-height:1.4}
.welcome-box strong{font-weight:400;font-size:20px}
.divider{left:0;top:914px;width:1200px;height:1px;background:var(--line)}
/* booking */
.book-title{left:132px;top:962px;font-size:34px;font-weight:300;color:var(--blue)}
.book-text{left:132px;top:1012px;width:590px;font-size:11.5px;line-height:1.65;color:#666}
.btn{top:1126px;height:44px;font-size:15px;display:flex;align-items:center;justify-content:center;border-radius:2px}
.btn-primary{left:132px;width:184px;background:var(--blue);color:#fff}
.btn-ghost{left:325px;width:113px;border:1px solid var(--blue);color:var(--blue)}
.phone-art{left:807px;top:958px;width:196px;height:226px;border-radius:20px;background:linear-gradient(160deg,#2a2a2a,#555 60%,#b9dbee)}
/* services */
.services{left:0;top:1229px;width:1200px;height:552px;background:var(--grey-bg)}
.services-title{left:0;top:1260px;width:1200px;text-align:center;font-size:32px;font-weight:400;color:var(--green)}
.service-card{width:220px;height:192px}
.service-photo{height:151px}
.service-label{height:41px;background:var(--blue);color:#fff;font-size:15px;font-weight:600;padding:9px 14px}
/* testimonials */
.testi-title{left:0;top:1815px;width:1200px;text-align:center;font-size:38px;font-weight:700;color:#d3d3d3}
.testi-quote{left:0;top:1881px;width:1200px;text-align:center;font-size:20px;color:#333}
.testi-quote b{color:#bbb;font-size:30px;vertical-align:-6px;margin:0 12px;font-family:Georgia,serif}
.testi-name{left:0;top:1922px;width:1200px;text-align:center;font-size:15px;color:#444}
.dots{left:556px;top:1966px;display:flex;gap:16px}
.dots i{width:8px;height:8px;border-radius:50%;background:#bbb}
.dots i:first-child{background:var(--green)}
/* contact */
.map{left:0;top:2015px;width:600px;height:247px;background:linear-gradient(135deg,#d7d7d7,#c4c4c4 50%,#dcdcdc)}
.contact-panel{left:600px;top:2015px;width:600px;height:247px;background:var(--grey-bg)}
.contact-title{left:649px;top:2040px;font-size:23px;color:#333}
.field{width:181px;height:36px;background:#fff;font-size:11.5px;color:#777;padding:11px 17px}
.submit{background:#2d2d2d;color:#fff;text-align:center;padding-left:0}
/* footer */
.footer{left:0;top:2262px;width:1200px;height:144px;background:var(--dark);color:#cfcfcf}
.f-item{top:2287px;font-size:11.5px;display:flex;align-items:center;gap:12px}
.f-rule{left:132px;top:2323px;width:935px;height:1px;background:#4a4c50}
.f-links{left:132px;top:2344px;font-size:10px}
.f-copy{left:132px;top:2369px;font-size:10px}
.socials{left:963px;top:2289px;display:flex;gap:14px}
.socials i{width:11px;height:11px;border-radius:50%;background:#888}
.f-booking{left:793px;top:2355px;font-size:10px;display:flex;align-items:center;gap:14px}
.f-booking strong{font-size:20px;font-weight:600;color:#bbb}
</style>
</head>
<body>
<div class="abs top-rule"></div>

<header>
  <div class="abs brand">
    <div class="brand-mark"></div>
    <div class="brand-name">The Harbourlight<small>DENTAL CENTRE</small></div>
  </div>
  <div class="abs header-info"><span>Suite 9, 18 Tidewater Parade, Westhaven, WA 6190.</span><span>OPEN 8 AM TO 8PM 7 DAYS A WEEK</span></div>
  <div class="abs header-contact">
    <span><svg width="13" height="13" viewBox="0 0 24 24"><path fill="#1ba9e1" d="M6.6 10.8a15 15 0 006.6 6.6l2.2-2.2c.3-.3.7-.4 1-.2 1.1.4 2.3.6 3.6.6.6 0 1 .4 1 1V20c0 .6-.4 1-1 1A17 17 0 013 4c0-.6.4-1 1-1h3.5c.6 0 1 .4 1 1 0 1.3.2 2.5.6 3.6.1.3 0 .7-.2 1z"/></svg>08 5550 1420</span>
    <span><svg width="15" height="12" viewBox="0 0 24 18"><path fill="#1ba9e1" d="M0 0h24v18H0zM2 2l10 7 10-7z"/></svg>hello@harbourlight-dental.example</span>
  </div>
  <nav class="abs main-nav">
    <a class="active" style="width:117px">Home</a>
    <a style="width:150px">Meet the Team</a>
    <a style="width:316px">Dental Treatments/Walk-in Treatments</a>
    <a style="width:150px">Dental Advice</a>
    <a style="width:202px">Contact Us</a>
  </nav>
</header>

<section>
  <div class="abs hero" role="img" aria-label="Photo of the medical centre building front with the dental clinic entrance and parked cars"></div>
  <div class="abs hero-arrow" style="left:10px">&#8249;</div>
  <div class="abs hero-arrow" style="right:10px">&#8250;</div>
  <div class="abs strap-blue">We understand that everyone has a busy life and we<br>want dental treatment to be accessible for all.</div>
  <div class="abs strap-green">No Appointment Needed!</div>
</section>

<section>
  <div class="abs video-thumb" role="img" aria-label="Video still of a dentist treating a patient"></div>
  <div class="abs play"></div>
  <h1 class="abs welcome-title">Welcome to The Harbourlight Dental Centre</h1>
  <p class="abs welcome-text">Your general and cosmetic dentist in the heart of vibrant Westhaven. Whether it's cosmetic hygiene treatment, tooth whitening, or anti-wrinkle facial rejuvenation.<br>Located within the busy medical centre with free parking all around.</p>
  <div class="abs welcome-box">Please call or pop in and one of our helpful team will be only too happy to help for<br><strong>ALL YOUR DENTAL NEEDS.</strong></div>
  <div class="abs divider"></div>
</section>

<section>
  <h2 class="abs book-title">Find and Book Appointments, 24/7 with</h2>
  <p class="abs book-text">Nullam accumsan purus vel tempus viverra. Mauris suscipit felis id nunc elementum varius. Praesent elementum nulla sit amet justo pellentesque scelerisque. Nam et tortor in ante iaculis porttitor in luctus mi. Vivamus gravida sem a pretium euismod. Nam lobortis, purus et fringilla tempus, risus eros dignissim diam, eget finibus sem risus sit amet eros. Vestibulum facilisis dolor at purus tincidunt porta. Nam fringilla nulla vel nisl condimentum, dapibus condimentum enim porta.</p>
  <div class="abs btn btn-primary">Book Appointments</div>
  <div class="abs btn btn-ghost">Read more</div>
  <div class="abs phone-art" role="img" aria-label="Illustration of a smartphone showing the carely hub booking app"></div>
</section>

<section>
  <div class="abs services"></div>
  <h2 class="abs services-title">Our Services</h2>
  <div class="abs service-card" style="left:132px;top:1323px"><div class="service-photo" role="img" aria-label="Photo of a tooth extraction" style="background:linear-gradient(135deg,#3d4a6b,#9a5a5a)"></div><div class="service-label">Extractions</div></div>
  <div class="abs service-card" style="left:370px;top:1323px"><div class="service-photo" role="img" aria-label="Photo of dentists working on dentures" style="background:linear-gradient(135deg,#5b5550,#4a5d8a)"></div><div class="service-label">Dentures</div></div>
  <div class="abs service-card" style="left:608px;top:1323px"><div class="service-photo" role="img" aria-label="Photo of a filling treatment at an outdoor clinic" style="background:linear-gradient(135deg,#8b8478,#3f4a5e)"></div><div class="service-label">Fillings</div></div>
  <div class="abs service-card" style="left:846px;top:1323px"><div class="service-photo" role="img" aria-label="Photo of patients waiting for root canal treatment" style="background:linear-gradient(135deg,#b8b2a8,#4d5a70)"></div><div class="service-label">Root Canal Treatment</div></div>
  <div class="abs service-card" style="left:132px;top:1532px"><div class="service-photo" role="img" aria-label="Photo of a dental surgery chair" style="background:linear-gradient(135deg,#e6e6e2,#9fc38a)"></div><div class="service-label">Periodontal Treatment</div></div>
  <div class="abs service-card" style="left:370px;top:1532px"><div class="service-photo" role="img" aria-label="Photo of crown and bridge work" style="background:linear-gradient(135deg,#3d4760,#b69a9a)"></div><div class="service-label">Crowns and Bridges</div></div>
  <div class="abs service-card" style="left:608px;top:1532px"><div class="service-photo" role="img" aria-label="Photo of a teeth whitening session" style="background:linear-gradient(135deg,#5a5e6a,#3e4f78)"></div><div class="service-label">Teeth Whitening</div></div>
  <div class="abs service-card" style="left:846px;top:1532px"><div class="service-photo" role="img" aria-label="Photo of happy clinic patients" style="background:linear-gradient(135deg,#cfd6cc,#2f3b66)"></div><div class="service-label">Facial Aesthetics</div></div>
</section>

<section>
  <h2 class="abs testi-title">TESTIMONIALS</h2>
  <p class="abs testi-quote"><b>&ldquo;</b>Etiam quis magna nec odio sagittis pretium id eget risus eget fermentum magna arcu.<b>&rdquo;</b></p>
  <p class="abs testi-name">Mara Lindqvist, City</p>
  <div class="abs dots"><i></i><i></i><i></i><i></i></div>
</section>

<section>
  <div class="abs map" role="img" aria-label="Grey world map"></div>
  <div class="abs contact-panel"></div>
  <h2 class="abs contact-title" style="font-weight:400">Contact Us</h2>
  <div class="abs field" style="left:650px;top:2084px">First Name</div>
  <div class="abs field" style="left:842px;top:2084px">Last Name</div>
  <div class="abs field" style="left:650px;top:2132px">Phone</div>
  <div class="abs field" style="left:842px;top:2132px">Email</div>
  <div class="abs field" style="left:650px;top:2180px">City</div>
  <div class="abs field submit" style="left:842px;top:2180px">SUBMIT</div>
</section>

<footer>
  <div class="abs footer"></div>
  <div class="abs f-item" style="left:132px">
    <svg width="10" height="14" viewBox="0 0 10 14"><path fill="#aaa" d="M5 0a5 5 0 015 5c0 4-5 9-5 9S0 9 0 5a5 5 0 015-5zm0 3a2 2 0 100 4 2 2 0 000-4z"/></svg>Suite 9, 18 Tidewater Parade, Westhaven, WA 6190</div>
  <div class="abs f-item" style="left:493px">
    <svg width="12" height="12" viewBox="0 0 24 24"><path fill="#aaa" d="M6.6 10.8a15 15 0 006.6 6.6l2.2-2.2c.3-.3.7-.4 1-.2 1.1.4 2.3.6 3.6.6.6 0 1 .4 1 1V20c0 .6-.4 1-1 1A17 17 0 013 4c0-.6.4-1 1-1h3.5c.6 0 1 .4 1 1 0 1.3.2 2.5.6 3.6.1.3 0 .7-.2 1z"/></svg>Call Now: 08 5550 1420</div>
  <div class="abs f-item" style="left:676px">
    <svg width="14" height="11" viewBox="0 0 24 18"><path fill="#aaa" d="M0 0h24v18H0zM2 2l10 7 10-7z"/></svg>Email: hello@harbourlight-dental.example</div>
  <div class="abs socials"><i></i><i></i><i></i><i></i></div>
  <div class="abs f-rule"></div>
  <div class="abs f-links">Home &nbsp;|&nbsp; Meet the Team &nbsp;|&nbsp; Dental Treatments/Walk-in Treatments &nbsp;|&nbsp; Dental Advice &nbsp;|&nbsp; Contact us</div>
  <div class="abs f-copy">Copyright &copy; 2016 The Harbourlight Dental centre. All rights reserved.</div>
  <div class="abs f-booking">Appointment Booking <strong>carely hub</strong></div>
</footer>
</body>
</html>
```